Landing Page Design

Require a landing page design.

A wire concept has been provided along with a relevant logo and image files.

Target Market(s)

Facilities/Property Management companies
Maintenance Managers for manufacturing and related sites
Personal Assistants (those given responsible for the maintenance and cleaning of commercial properties

Industry/Entity Type

Construction

Number of Pages Required

1 page

Requirements
Must have
• 1. Layout as per wire design concept
2. Stick to colour scheme of logo and include plenty of white space
Should not have
• No flash

```html
<!DOCTYPE html>
<html lang="en">
<head>
<meta charset="utf-8">
<title>Norvale Property Services – Free Window &amp; Carpet Clean</title>
<link href="https://fonts.googleapis.com/css2?family=Arimo:ital,wght@0,400;0,700;1,400;1,700&display=swap" rel="stylesheet">
<style>
:root{
  --navy:#0b3a7a;
  --navy-deep:#062a5e;
  --blue:#0f5aa8;
  --green:#3a8a12;
  --green-bright:#5cbf1c;
  --text:#3d4450;
  --text-dark:#2c3240;
  --panel:#f2f3f6;
  --line:#d8dbe1;
  --white:#ffffff;
}
*{box-sizing:border-box;margin:0;padding:0}
html,body{width:857px;height:1200px;overflow:hidden;background:var(--white)}
body{font-family:"Arimo",Arial,sans-serif;color:var(--text);position:relative}
.header{position:absolute;left:52px;top:11px;width:770px;height:201px;border-radius:7px;overflow:hidden;
  background:linear-gradient(90deg,#0a3c86 0%,#0d4a97 45%,#0a3a7c 60%)}
.header-photo{position:absolute;right:0;top:0;width:360px;height:100%;
  background:linear-gradient(135deg,#c9d8ea 0%,#5f86b8 30%,#1f4d8d 60%,#163c73 100%);opacity:.9}
.header-photo::before{content:"";position:absolute;inset:0;background:linear-gradient(90deg,#0d4a97 0%,rgba(13,74,151,0) 35%)}
.brand{position:absolute;left:50px;top:30px;display:flex;align-items:center;gap:8px}
.brand-mark{width:30px;height:30px;background:var(--white)}
.brand-name{font-size:36px;font-weight:700;color:var(--white);letter-spacing:2px}
.brand-sub{position:absolute;left:150px;top:71px;font-size:13px;color:var(--white)}
.offer{position:absolute;left:23px;top:112px;color:var(--white);font-size:19px}
.offer b{font-weight:700;font-size:21px}
.offer .amp{font-size:27px;margin:0 2px}
.call-bar{position:absolute;left:26px;top:147px;width:336px;height:33px;border-radius:7px;
  background:linear-gradient(#ffffff,#c7d8ee);display:flex;align-items:center}
.call-icon{width:38px;height:38px;border-radius:5px;background:linear-gradient(#6fd22a,#2f8a0c);margin-left:12px;margin-top:-4px;display:flex;align-items:center;justify-content:center}
.call-bar span{margin-left:16px;font-size:18px;font-weight:700;color:var(--blue)}
.features{position:absolute;left:57px;top:227px;width:757px;height:38px;border:1px dashed #cfd3d9;border-left:none}
.feature{position:absolute;top:219px;display:flex;align-items:center;font-size:20px;color:#4a505c}
.feat-icon{width:42px;height:52px;margin-right:22px;flex:none}
.panel{position:absolute;left:52px;top:285px;width:769px;height:738px;background:var(--panel);border:1px solid var(--line);border-radius:6px}
.copy{position:absolute;left:74px;top:310px;width:452px;font-size:12.5px;line-height:18px;color:var(--text)}
.copy p{margin-bottom:18px}
.copy .lead{font-weight:700;color:var(--text-dark)}
.reasons-title{position:absolute;left:69px;top:591px;padding:3px 9px;border:1px solid #cfd3d9;border-radius:6px;background:var(--white);font-size:16.5px;font-weight:700;color:var(--green)}
.reasons{position:absolute;left:79px;top:636px;width:400px;list-style:none;font-size:12.5px;line-height:18px}
.reasons li{display:flex;gap:14px;min-height:53px}
.reasons li.single{min-height:45px}
.tick{width:24px;height:24px;flex:none;margin-top:2px}
.btn{position:absolute;top:883px;height:45px;border-radius:6px;background:linear-gradient(#1d6cbe,#0a3f87);border:2px solid #bcd1ec;box-shadow:0 0 0 1px #0a3f87;color:var(--white);font-size:17px;font-weight:700;display:flex;align-items:center;justify-content:center}
.closing{position:absolute;left:79px;top:942px;width:370px;text-align:center;font-size:12.5px;line-height:18px;font-weight:700;color:var(--text-dark)}
.form-card{position:absolute;left:558px;top:302px;width:250px;height:444px;background:var(--white);border:1px solid var(--line)}
.form-head{height:128px;background:linear-gradient(#0e4b99,#0a3a7c);border-radius:5px 5px 0 0;color:var(--white);text-align:center;padding-top:15px}
.form-head .intro{font-size:12.5px;font-weight:700;line-height:18px}
.form-head .phone{font-size:28px;font-weight:700;margin-top:7px;letter-spacing:1px}
.form-head .reg{font-size:11.5px;font-weight:700;margin-top:10px;padding-top:6px;border-top:1px solid rgba(255,255,255,.25)}
.form{padding:14px 14px 0}
.form label{display:block;font-size:11.5px;font-weight:700;color:var(--text-dark);margin-bottom:8px}
.field{height:30px;border:1px solid #c8ccd3;border-radius:6px;font-size:11.5px;color:var(--text);padding:0 12px;display:flex;align-items:center;margin-bottom:14px}
.register{margin:2px 0 0 2px;width:150px;height:39px;border-radius:6px;background:linear-gradient(#1d6cbe,#0a3f87);border:2px solid #bcd1ec;box-shadow:0 0 0 1px #0a3f87;color:var(--white);font-size:16px;font-weight:700;display:flex;align-items:center;justify-content:center}
.quote{position:absolute;left:557px;top:755px;width:249px;height:74px;background:var(--white);border:1px solid var(--line);border-radius:7px;padding:16px 15px;font-size:14px;line-height:21px;font-style:italic;font-weight:700;color:#6c7180}
.quote::after{content:"";position:absolute;left:55px;bottom:-9px;width:14px;height:14px;background:var(--white);border-right:1px solid var(--line);border-bottom:1px solid var(--line);transform:rotate(45deg)}
.quote-by{position:absolute;left:567px;top:845px;font-size:11px;color:#5a6070;text-decoration:underline}
</style>
</head>
<body>
<header class="header">
  <div class="header-photo" role="img" aria-label="Photo of window cleaners on ladders at a glass office building"></div>
  <div class="brand"><div class="brand-mark"></div><div class="brand-name">NORVALE</div></div>
  <div class="brand-sub">Property Services Group</div>
  <div class="offer"><b>FREE</b> WINDOW <span class="amp">&amp;</span> CARPET CLEAN</div>
  <div class="call-bar">
    <div class="call-icon"><svg width="24" height="24" viewBox="0 0 24 24"><path d="M6 3l4 4-2 3c1 3 3 5 6 6l3-2 4 4-3 3C10 21 3 14 3 6z" fill="none" stroke="#fff" stroke-width="2"/></svg></div>
    <span>Call Now On 1300 55 01 88</span>
  </div>
</header>

<div class="features"></div>
<div class="feature" style="left:57px">
  <svg class="feat-icon" viewBox="0 0 42 52"><rect x="2" y="2" width="36" height="48" fill="#fff" stroke="#c9ccd2"/><g stroke="#b9bec6"><line x1="7" y1="10" x2="25" y2="10"/><line x1="7" y1="18" x2="33" y2="18"/><line x1="7" y1="24" x2="33" y2="24"/><line x1="7" y1="30" x2="33" y2="30"/><line x1="7" y1="36" x2="33" y2="36"/></g><path d="M24 6l12 12M36 6L24 18" stroke="#d8232a" stroke-width="4"/></svg>
  No Contracts
</div>
<div class="feature" style="left:257px">
  <svg class="feat-icon" viewBox="0 0 52 52" style="width:52px;margin-right:14px"><circle cx="26" cy="26" r="24" fill="#3aa312"/><circle cx="26" cy="26" r="20" fill="#5cc522"/><path d="M18 22a10 10 0 1 0 8-6" fill="none" stroke="#fff" stroke-width="4"/><path d="M24 10l6 6-7 4z" fill="#fff"/></svg>
  Routine Office Cleaning
</div>
<div class="feature" style="left:548px">
  <svg class="feat-icon" viewBox="0 0 56 52" style="width:56px;margin-right:18px"><ellipse cx="28" cy="44" rx="26" ry="6" fill="#e3e5e9"/><path d="M12 12h30l-3 28H15z" fill="#f4f5f7" stroke="#d3d6dc"/><ellipse cx="27" cy="12" rx="15" ry="4" fill="#6b3d1a"/></svg>
  Painless Experience
</div>

<main class="panel"></main>

<section class="copy">
  <p class="lead">Engage our routine office cleaning for at least 6 months and receive a FREE Carpet and Window clean! No strings attached, no contracts</p>
  <p class="lead">To takeadvantage of this great offer call us on 1300 55 01 88 or complete and submit theform on this page.</p>
  <p>At Norvale we provide all your property service needs - painlessly. We understand that cleaning andother property services should be background activities. A set and forget proposition.</p>
  <p>We also know that youshould not have to police or project manage our Service Teams.</p>
  <p>After engaging Norvale, property services will become your lowest<br>priority, as it is our highest priority.</p>
</section>

<div class="reasons-title">Top Five Reasons to Choose Norvale</div>
<ul class="reasons">
  <li><svg class="tick" viewBox="0 0 24 24"><circle cx="12" cy="12" r="11" fill="#fff" stroke="#d8dbe1"/><path d="M6 12l4 4 8-9" fill="none" stroke="#3aa312" stroke-width="3"/></svg>We self audit and performance manage our Service Teams while they're on the job</li>
  <li><svg class="tick" viewBox="0 0 24 24"><circle cx="12" cy="12" r="11" fill="#fff" stroke="#d8dbe1"/><path d="M6 12l4 4 8-9" fill="none" stroke="#3aa312" stroke-width="3"/></svg>We minimise contact time required between the client and our Service Teams</li>
  <li><svg class="tick" viewBox="0 0 24 24"><circle cx="12" cy="12" r="11" fill="#fff" stroke="#d8dbe1"/><path d="M6 12l4 4 8-9" fill="none" stroke="#3aa312" stroke-width="3"/></svg>Our Service Teams are proactive in identifying irregular<br>requirements</li>
  <li class="single"><svg class="tick" viewBox="0 0 24 24"><circle cx="12" cy="12" r="11" fill="#fff" stroke="#d8dbe1"/><path d="M6 12l4 4 8-9" fill="none" stroke="#3aa312" stroke-width="3"/></svg>We have a comprehensive Health Safety Management system</li>
  <li class="single"><svg class="tick" viewBox="0 0 24 24"><circle cx="12" cy="12" r="11" fill="#fff" stroke="#d8dbe1"/><path d="M6 12l4 4 8-9" fill="none" stroke="#3aa312" stroke-width="3"/></svg>We can provide our Property Services on a National basis</li>
</ul>

<div class="btn" style="left:78px;width:175px">Book a Free Quote</div>
<div class="btn" style="left:273px;width:175px">Visit Our Website</div>

<p class="closing">If you would like to join our growing list of satisfied clients, call NOW to discuss how Norvale can best meet all your Commercial Cleaning and Property Service needs.</p>

<aside class="form-card">
  <div class="form-head">
    <div class="intro">TAKE ADVANTAGE OF THIS GREAT<br>OFFER. CONTACT US NOW ON</div>
    <div class="phone">1300 55 01 88</div>
    <div class="reg">OR REGISTER YOUR INTEREST BELOW</div>
  </div>
  <div class="form">
    <label>NAME:</label><div class="field">Daniel Hartley</div>
    <label>BUSINESS NAME:</label><div class="field">Daniel Hartley</div>
    <label>EMAIL:</label><div class="field">d.hartley@example.com</div>
    <label>EMAIL:</label><div class="field">1-555-010-2244</div>
    <div class="register">Register</div>
  </div>
</aside>

<blockquote class="quote">“Truly outstanding service, job well done! 100% Satisfied”</blockquote>
<div class="quote-by">Posted By Laura Whitfield of Brightway Co</div>
</body>
</html>
```